Webdesign für die Korvelt GmbH
Zielgruppe
Beratung • Renovierung • Reparatur • Planung • Bau • Pflege • Wartung im Bereich der Haustechnik
Aufgabenstellung
Bilder nur von bildmoro oder von der Webseite des Kunden nutzen

```html
<!DOCTYPE html>
<html lang="de">
<head>
<meta charset="utf-8">
<title>Korvelt Heizung-Sanitär GmbH</title>
<link href="https://fonts.googleapis.com/css2?family=Comfortaa:wght@400;700&family=Open+Sans:ital,wght@0,400;0,700;1,400&display=swap" rel="stylesheet">
<style>
:root{
  --blue:#1a7fc4;
  --blue-dark:#0d6fb8;
  --blue-mid:#2a9fdf;
  --blue-light:#4fc9d8;
  --steel:#4a86c4;
  --sky:#8fc3e3;
  --red:#d9272e;
  --text:#555;
  --band:#f6f6f6;
  --grey:#ececec;
}
*{margin:0;padding:0;box-sizing:border-box}
html,body{width:909px;height:1200px;overflow:hidden;background:#fff}
body{position:relative;font-family:"Open Sans",sans-serif;color:var(--text)}
.abs{position:absolute}
.round{font-family:"Comfortaa",sans-serif}

.topbar{left:0;top:0;width:909px;height:16px;background:#f7f7f7;font-size:6px;color:#666}
.topbar span{position:absolute;top:4px;display:flex;align-items:center;gap:3px}
.dot{width:6px;height:6px;border-radius:50%;background:#666;display:inline-block}

.brand{left:165px;top:37px;font-size:9.5px;color:var(--blue)}
.brand b{font-weight:700}
.btn-contact{left:682px;top:35px;width:49px;height:18px;background:var(--red);color:#fff;font-size:8px;font-weight:700;display:flex;align-items:center;justify-content:center;border-radius:1px}

.nav{left:0;top:71px;width:909px;height:25px;background:#f7f7f7}
.nav .home{position:absolute;left:165px;top:0;width:30px;height:25px;background:#ececec;display:flex;align-items:center;justify-content:center}
.nav a{position:absolute;top:9px;font-size:6.4px;color:var(--blue);text-decoration:none;letter-spacing:.1px}

.hero{left:0;top:96px;width:909px;height:239px;background:linear-gradient(90deg,#d9b89a 0%,#c89a78 25%,#e8e8e8 45%,#d8dcdf 70%,#b9bec2 100%)}
.logo-box{left:157px;top:314px;width:148px;height:41px;background:#fff;display:flex;align-items:center;justify-content:center;gap:6px;font-size:19px;line-height:1;font-weight:700;color:var(--blue);z-index:5}
.logo-box i{width:9px;height:9px;background:var(--red);display:inline-block}

.features{left:0;top:335px;width:909px;height:39px;background:var(--band)}
.features .sep{position:absolute;top:0;width:1px;height:39px;background:#e2e2e2}
.feat{position:absolute;top:9px;font-size:9px;color:#444}
.feat small{display:block;font-family:"Open Sans",sans-serif;font-size:6px;color:#888;line-height:6px}

.tiles{left:0;top:374px;width:909px;height:160px;background:var(--grey)}
.tile{position:absolute;top:11px;width:163px;height:134px;display:flex;justify-content:center;color:#fff;font-size:24px}
.tile span{margin-top:44px}
.t1{left:179px;background:linear-gradient(135deg,#0fa4e4,#0a86d2)}
.t2{left:374px;background:linear-gradient(135deg,#2aa9e8,#36b9ee)}
.t3{left:567px;background:linear-gradient(135deg,#58cfe0,#3fbccf)}

.welcome{left:179px;top:535px;font-size:17px;font-weight:700;color:var(--blue)}
.about{left:0;top:555px;width:909px;height:96px;background:var(--band)}
.about p{position:absolute;left:179px;top:12px;width:314px;font-size:8.6px;line-height:17px;text-align:justify;color:#555}
.exp{position:absolute;left:639px;top:12px;width:90px;height:71px;background:var(--blue-dark);color:#fff;padding:4px 5px;font-size:8.8px;line-height:13.5px}
.exp em{display:block;font-size:11px;margin-bottom:4px}

.partner{left:0;top:668px;width:909px;text-align:center;font-size:8.8px;line-height:12.5px;color:#555}
.partner b{color:var(--blue);font-weight:400;margin:0 4px}

.formband{left:0;top:708px;width:909px;height:278px;background:linear-gradient(180deg,#d9d3c9 0%,#e4ddd2 45%,#c48a4c 80%,#b77a3e 100%)}
.form{left:179px;top:731px;width:265px;height:208px;background:rgba(255,255,255,.55)}
.form label{position:absolute;left:10px;font-size:8.5px;color:#666}
.form label b{color:#555}
.form .field{position:absolute;left:9px;width:242px;height:22px;background:rgba(255,255,255,.8);border:1px solid var(--steel)}
.form .send{position:absolute;left:201px;top:173px;width:50px;height:23px;background:var(--steel);color:#fff;font-size:7.5px;font-weight:700;display:flex;align-items:center;justify-content:center}

.services{left:0;top:986px;width:909px;height:150px;background:#f5f5f5}
.svc{position:absolute;width:85px;height:55px;color:#fff;font-size:9.5px;font-weight:700;line-height:13px;display:flex;align-items:center;padding-left:8px}
.svc-text{position:absolute;font-size:9.6px;line-height:16.5px;color:#555}
.vline{position:absolute;width:1px;height:26px;background:#999}

.footer{left:0;top:1145px;width:909px;height:55px;background:#fff;font-size:8.6px;color:#555}
.footer span{position:absolute;top:22px;display:flex;align-items:center;gap:3px}
.footer .small{font-family:"Comfortaa",sans-serif;font-size:6px;top:24px}
</style>
</head>
<body>

<div class="abs topbar round">
  <span style="left:166px"><i class="dot"></i></span>
  <span style="left:194px"><svg width="11" height="7" viewBox="0 0 11 7"><rect x=".5" y=".5" width="10" height="6" fill="none" stroke="#666"/><path d="M.5 .5 5.5 4 10.5 .5" fill="none" stroke="#666"/></svg>info@korvelt-gmbh.de</span>
  <span style="left:316px"><svg width="8" height="8" viewBox="0 0 8 8"><path d="M1 1c1-1 2 0 2 1s-1 1 0 2 1 1 2 0 2 0 2 1-1 2-2 2C3 7 1 5 1 1z" fill="#666"/></svg>03740-5182-0</span>
  <span style="left:393px"><svg width="7" height="5" viewBox="0 0 7 5"><rect width="7" height="1.7" fill="#222"/><rect y="1.7" width="7" height="1.6" fill="#d00"/><rect y="3.3" width="7" height="1.7" fill="#fc0"/></svg>&nbsp;08412 Birkental / Erzg.</span>
</div>

<div class="abs brand round">Korvelt <b>Heizung-Sanitär GmbH</b></div>
<div class="abs btn-contact">Kontakt</div>

<nav class="abs nav round">
  <div class="home"><svg width="11" height="10" viewBox="0 0 11 10"><path d="M5.5 0 11 5H9.5v5h-3V7h-2v3h-3V5H0z" fill="var(--red)"/></svg></div>
  <a style="left:207px">MENÜ1</a>
  <a style="left:242px">MENÜ-ABC-TEXT-BEISPIEL</a>
  <a style="left:342px">MENÜ-3-TEXT</a>
  <a style="left:401px">MENÜ-TITEL-2-TEXT</a>
  <a style="left:481px">MENÜ-4-TEXT</a>
  <a style="left:540px">MENÜ-5-TEXT</a>
</nav>

<div class="abs hero" role="img" aria-label="Foto einer lachenden Frau nach dem Duschen neben einem modernen Bad mit freistehender Badewanne">
  <svg width="909" height="239" viewBox="0 0 909 239" style="position:absolute;left:0;top:0">
    <path d="M456 0C430 110 360 190 268 239" fill="none" stroke="#fff" stroke-width="2"/>
  </svg>
</div>

<section class="abs features round">
  <div class="sep" style="left:339px"></div>
  <div class="sep" style="left:519px"></div>
  <svg style="position:absolute;left:367px;top:12px" width="13" height="13" viewBox="0 0 13 13"><circle cx="6.5" cy="6.5" r="6" fill="#3ab54a"/><circle cx="4.5" cy="5" r="1" fill="#1a5a20"/><circle cx="8.5" cy="5" r="1" fill="#1a5a20"/><path d="M3.5 7.5Q6.5 10.5 9.5 7.5" fill="none" stroke="#1a5a20"/></svg>
  <div class="feat" style="left:386px">Erfahrung in 3. Generation<small>seit 01. Juni 1949</small></div>
  <svg style="position:absolute;left:550px;top:12px" width="15" height="14" viewBox="0 0 15 14"><path d="M7.5 0 9.3 5H15l-4.6 3.3 1.7 5.5-4.6-3.4-4.6 3.4 1.7-5.5L0 5h5.7z" fill="#f5b21a"/></svg>
  <div class="feat" style="left:570px">Handwerksqualität<small>fachgerechte Umsetzung Ihrer Wünsche</small></div>
</section>

<div class="abs logo-box"><i></i>KORVELT</div>

<section class="abs tiles round">
  <svg style="position:absolute;left:110px;top:52px" width="41" height="51" viewBox="0 0 41 51"><path d="M40 1 2 25.5 40 50" fill="none" stroke="var(--blue-mid)" stroke-width="5" stroke-dasharray="1.5 2"/><path d="M32 6 10 25.5 32 45" fill="none" stroke="var(--blue-mid)" stroke-width="3" stroke-dasharray="1.5 2"/></svg>
  <div class="tile t1"><span>Wärme</span></div>
  <div class="tile t2"><span style="margin-top:47px">Wasser</span></div>
  <div class="tile t3"><span style="margin-top:47px">Luft</span></div>
  <svg style="position:absolute;left:758px;top:52px" width="41" height="51" viewBox="0 0 41 51"><path d="M1 1 39 25.5 1 50" fill="none" stroke="var(--blue-mid)" stroke-width="5" stroke-dasharray="1.5 2"/><path d="M9 6 31 25.5 9 45" fill="none" stroke="var(--blue-mid)" stroke-width="3" stroke-dasharray="1.5 2"/></svg>
</section>

<h1 class="abs welcome">Herzlich Willkommen</h1>
<section class="abs about">
  <p>Wenn Sie einen zuverlässigen Partner für die Erledigung Ihrer Aufträge suchen, Wert auf Kreativität und Freundlichkeit legen, dann sind Sie bei uns an der richtigen Stelle. Vom ersten Beratungsgespräch bis zur Übergabe der fertiggestellten Leistung, sollten Sie, wie viele Kunden vor Ihnen, gute Erfahrungen mit uns machen.</p>
  <div class="exp"><em>Erfahrung</em>1949 - 2019<br>über <b>65 Jahre</b><br>Firma Korvelt</div>
</section>

<div class="abs partner round">Wir sind Ihr zuverlässiger Partner bei Arbeiten rund um<br><b>Wärme</b><b>Wasser</b><b>Luft</b><b>Dach</b>und <b style="margin:0">Service</b>.</div>

<div class="abs formband" role="img" aria-label="Foto eines hellen Badezimmers mit Holzwand, freistehender Wanne, Pflanzen und Holzboden"></div>
<form class="abs form">
  <label style="top:10px">Ihr <b>Name</b></label>
  <div class="field" style="top:23px"></div>
  <label style="top:47px">Ihre <b>Telefonnummer</b></label>
  <div class="field" style="top:59px"></div>
  <label style="top:91px">Ihr <b>Anliegen</b></label>
  <div class="field" style="top:104px"></div>
  <label style="top:129px">Ihre <b>Nachricht</b></label>
  <div class="field" style="top:140px"></div>
  <div class="send">Senden</div>
</form>

<section class="abs services">
  <div class="svc" style="left:106px;top:16px;background:var(--steel);padding-left:6px">Wir beraten Sie</div>
  <div class="svc-text" style="left:199px;top:17px">bei der Neuerstellung Ihrer Heizungs-, Sanitär-, Klimaanlage<br>bei der Sanierung und Modernisierung</div>
  <div class="svc" style="left:106px;top:80px;background:var(--blue-dark);padding-left:17px">planen<br>und bauen</div>
  <div class="svc-text" style="left:199px;top:80px">Warmwasser-, Dampfheizanlagen<br>Lüftungs-, Klimaanlagen</div>
  <div class="vline" style="left:347px;top:88px"></div>
  <div class="svc-text" style="left:354px;top:80px">Fußboden-, Wand- und<br>Deckenheizungen</div>
  <div class="svc" style="left:474px;top:16px;background:var(--blue-mid);line-height:16.5px">renovieren<br>und reparieren</div>
  <div class="svc-text" style="left:575px;top:17px">Heizungs-, Lüftungs- und Sanitäranlagen in Wohn- und<br>Industriegebäuden, in Schulen und Freizeitanlagen</div>
  <div class="svc" style="left:474px;top:81px;background:var(--sky);line-height:16.5px">pflegen<br>und warten</div>
  <div class="svc-text" style="left:575px;top:71px">alle Heizungs-, Lüftungs- und Sanitäranlagen und<br>bieten Ihnen darüber hinaus Wartungsverträge für alle<br>genannten Bereiche</div>
</section>

<footer class="abs footer">
  <span style="left:106px">Korvelt&nbsp;<b>Heizung-Sanitär GmbH</b></span>
  <span style="left:265px">Lindenweg 14</span>
  <span style="left:367px">08412 Birkental / Erzg.</span>
  <span style="left:477px;top:25px"><i class="dot"></i></span>
  <span class="small" style="left:504px"><svg width="11" height="7" viewBox="0 0 11 7"><rect x=".5" y=".5" width="10" height="6" fill="none" stroke="#666"/><path d="M.5 .5 5.5 4 10.5 .5" fill="none" stroke="#666"/></svg>info@korvelt-gmbh.de</span>
  <span class="small" style="left:626px"><svg width="8" height="8" viewBox="0 0 8 8"><path d="M1 1c1-1 2 0 2 1s-1 1 0 2 1 1 2 0 2 0 2 1-1 2-2 2C3 7 1 5 1 1z" fill="#666"/></svg>03740-5182-0</span>
</footer>

</body>
</html>
```